Decorative concrete business needs new business cards

Our company attracts homeowners and business with disposable cash. We are a artistic decorative coatings company that will transform your driveway, patio, floors or counter tops into a work of art. We also engrave logos and designs right into the concrete! We are upscale and very professional company. I am open for rearranging our logo on the business card and also to different color patterns. We like the blue and black as in Marlowbeck's logo. We also like blue and orange/yellow.

Target Market(s)

Adults 30-70

Industry/Entity Type

Concrete

Contact Information for Business Card

Simple: Name, phone, email, website and social media icons

Font styles to use
Serif

Colors

Designer to choose colors to be used in the design.

Requirements
Must have
• Must present a professional upscale appearance. I have attached before and after photos that show you what our industry does. Maybe I will have before and after photo on back of card.
Nice to have
• Artistic, but bold. Nothing whimsical or cute.
Should not have
• Should not have cartoon or childlike appearance.

```html
<!DOCTYPE html>
<html lang="en">
<head>
<meta charset="utf-8">
<title>Stonevale Finishes – Business Card</title>
<link href="https://fonts.googleapis.com/css2?family=Cinzel:wght@500&family=Oswald:wght@500&family=Open+Sans:wght@400&display=swap" rel="stylesheet">
<style>
  :root {
    --page: #2b2b2d;
    --card: #1d1d1e;
    --ink-white: #f4f4f4;
    --ink-grey: #c9c9c9;
    --ink-logo: #8a8a8c;
    --accent-blue: #2b8fd0;
    --social-violet: #a23fb8;
    --divider: #6d6d6f;
  }
  * { margin: 0; padding: 0; box-sizing: border-box; }
  html, body { width: 1200px; height: 1000px; overflow: hidden; }
  body {
    background: var(--page);
    font-family: "Open Sans", Arial, sans-serif;
    position: relative;
  }
  .card {
    position: absolute;
    left: 250px;
    width: 700px;
    height: 400px;
    background: var(--card);
    box-shadow: 0 14px 30px rgba(0,0,0,0.45);
  }
  .card--front { top: 60px; }
  .card--back { top: 540px; }

  /* front */
  .brand {
    position: absolute;
    left: 50%; top: 50%;
    transform: translate(-50%, -50%);
    display: flex;
    align-items: center;
    gap: 18px;
  }
  .brand__mark {
    width: 54px; height: 54px;
    background: var(--ink-logo);
  }
  .brand__name {
    font-family: "Cinzel", Georgia, serif;
    font-weight: 500;
    font-size: 40px;
    line-height: 1.05;
    color: var(--ink-logo);
    letter-spacing: 2px;
  }

  /* back */
  .identity {
    position: absolute;
    right: 380px;
    top: 135px;
    text-align: right;
  }
  .identity__name {
    font-family: "Oswald", "Arial Narrow", sans-serif;
    font-weight: 500;
    font-size: 42px;
    color: var(--ink-white);
    letter-spacing: 1px;
    line-height: 1.1;
  }
  .identity__role {
    font-size: 22px;
    color: var(--accent-blue);
    letter-spacing: 1px;
    margin-top: 2px;
  }
  .divider {
    position: absolute;
    left: 338px; top: 138px;
    width: 2px; height: 88px;
    background: var(--divider);
  }
  .contacts {
    position: absolute;
    left: 360px; top: 132px;
    list-style: none;
    font-size: 18px;
    color: var(--ink-grey);
  }
  .contacts li {
    display: flex;
    align-items: center;
    gap: 14px;
    height: 27px;
  }
  .contacts svg { width: 15px; height: 15px; fill: var(--accent-blue); flex: none; }
  .contacts .link { color: var(--accent-blue); }
  .social { gap: 10px !important; }
  .social__dots { display: flex; gap: 6px; margin-left: 10px; }
  .social__dot { width: 16px; height: 16px; border-radius: 50%; background: var(--accent-blue); }
  .social__dot--violet { background: var(--social-violet); }
  .address {
    position: absolute;
    left: 250px; top: 312px;
    display: flex;
    align-items: center;
    gap: 12px;
    font-size: 19px;
    color: var(--ink-grey);
    letter-spacing: 0.5px;
  }
  .address svg { width: 16px; height: 20px; fill: var(--accent-blue); }
</style>
</head>
<body>
  <section class="card card--front">
    <div class="brand">
      <div class="brand__mark"></div>
      <div class="brand__name">Stonevale<br>Finishes</div>
    </div>
  </section>

  <section class="card card--back">
    <div class="identity">
      <div class="identity__name">ADRIAN KELLNER</div>
      <div class="identity__role">CEO</div>
    </div>
    <div class="divider"></div>
    <ul class="contacts">
      <li>
        <svg viewBox="0 0 24 24"><path d="M6.6 10.8a15.1 15.1 0 0 0 6.6 6.6l2.2-2.2c.3-.3.7-.4 1-.2 1.1.4 2.3.6 3.6.6.6 0 1 .4 1 1V20c0 .6-.4 1-1 1A17 17 0 0 1 3 4c0-.6.4-1 1-1h3.5c.6 0 1 .4 1 1 0 1.3.2 2.5.6 3.6.1.3 0 .7-.2 1z"/></svg>
        +000 555 014 272
      </li>
      <li>
        <svg viewBox="0 0 24 24"><path d="M2 5h20v14H2z M3 6l9 7 9-7" /><path d="M2 5l10 8 10-8v14H2z"/></svg>
        adrian@stonevale.com
      </li>
      <li>
        <svg viewBox="0 0 24 24"><circle cx="12" cy="12" r="10"/></svg>
        <span>www.<span class="link">stonevalefinishes</span>.com</span>
      </li>
      <li class="social">
        Follow On
        <span class="social__dots">
          <span class="social__dot social__dot--violet"></span>
          <span class="social__dot"></span>
          <span class="social__dot"></span>
        </span>
      </li>
    </ul>
    <div class="address">
      <svg viewBox="0 0 16 20"><path d="M8 0a7 7 0 0 0-7 7c0 5 7 13 7 13s7-8 7-13a7 7 0 0 0-7-7zm0 10a3 3 0 1 1 0-6 3 3 0 0 1 0 6z"/></svg>
      Your Street Address, Harbourton, 1234
    </div>
  </section>
</body>
</html>
```